The Maple Arch Dental Offices Double-Sided A5 Flyer Highlighting Strengths & All Locations.

Designs are looking good. I just feel that they're too much in terms of content. Slight change in strategy. I would like a double sided A5 Flyer that has the following:

Front Side:

1. Brand (The Maple Arch Dental Offices). Use the logo that has Dental Offices beneath the words "The Maple Arch."
2. Highlight only the following keywords: Affordable. Friendly. Experienced Dental Care. Kids Friendly. We Accept All Insurance. 0% Interest Payment Plans.
3. Dental Services: Family Dentistry, Teeth Whitening, Braces, Implants, Veneers, Sedation.

Back Side:

This is where I want to highlight how convenient The Maple Arch is. We have 15 locations and growing. So here you can use our tagline:

We're Always Close By! With 15 Locations and Counting.

I want to list all 15 locations with each locations address and unique number. You can find those at https://maplearchsmiles.com/locations
The designer that can provide all locations in a catchy, easy to read and clean design will be selected.

The base of the flyer should utilize a white background. Keep it clean. Keep it fresh.

I'm looking to stand out from all competition with something unique and different. Get creative.

Target Market(s)

Women 30-40 years of age.

Industry/Entity Type

Dental

Font styles to use
Sans Serif

Colors
86cfc6
33b8a4
00a990
f59195
fdfdfb
fdf9cf
dddddd

Requirements
Must have
• Proper brand and color elements. Use white background.
Nice to have
• Surprise me with great ideas and design.
Should not have
• Prices.

```html
<!DOCTYPE html>
<html lang="en">
<head>
<meta charset="utf-8">
<title>The Maple Arch Dental Offices – A5 Flyer</title>
<link rel="stylesheet" href="https://fonts.googleapis.com/css2?family=Advent+Pro:wght@300;400&family=Antonio:wght@700&family=Oswald:wght@500;600&family=Pathway+Gothic+One&family=Quicksand:wght@500&family=Open+Sans:wght@400;600;700&display=swap">
<style>
  :root{
    --teal:#00a990;
    --teal-mid:#33b8a4;
    --teal-soft:#86cfc6;
    --teal-pale:#d3eeea;
    --white:#fdfdfb;
    --cream:#fdf9cf;
    --pink:#f59195;
    --grey:#dddddd;
    --ink:#5a5a5a;
    --ink-soft:#8a8a8a;
    --stage:#cfcfcf;
  }
  *{box-sizing:border-box;margin:0;padding:0}
  html,body{width:1200px;height:960px;overflow:hidden}
  body{background:var(--stage);font-family:"Open Sans",sans-serif;position:relative}
  .flyer{position:absolute;top:90px;width:552px;height:780px;background:var(--white);overflow:hidden;box-shadow:0 10px 28px rgba(0,0,0,.18)}
  .flyer--front{left:32px}
  .flyer--back{left:616px}
  .abs{position:absolute}

  /* brand */
  .brand{display:flex;flex-direction:column;align-items:center;color:var(--ink)}
  .brand__mark{width:34px;height:34px;border-radius:50%;background:var(--teal-soft);margin-bottom:6px}
  .brand__name{font-family:"Quicksand",sans-serif;font-weight:500;font-size:27px;line-height:1;color:var(--ink)}
  .brand__sub{font-family:"Quicksand",sans-serif;font-weight:500;font-size:8px;letter-spacing:2px;color:var(--ink);margin-top:4px}

  /* front */
  .front-brand{left:18px;top:28px;width:240px}
  .call-box{right:0;top:28px;width:256px;height:92px;background:var(--teal);color:#fff;padding:22px 14px 0 18px}
  .call-box__rule{position:absolute;left:8px;right:8px;top:8px;border-top:1.5px dashed rgba(255,255,255,.8)}
  .call-box__phone{font-size:19px;letter-spacing:.5px}
  .call-box__web{font-size:17px;letter-spacing:.5px;margin-top:2px;white-space:nowrap}
  .call-box__shadow{right:40px;top:120px;width:216px;height:14px;background:linear-gradient(90deg,var(--teal-pale),rgba(211,238,234,0))}
  .hero-photo{left:22px;top:170px;width:226px;height:226px;border-radius:50%;background:radial-gradient(circle at 50% 40%,#e9c7ae,#a97d5f 70%,#6d5446);border:4px solid #f1f1f1}
  .headline{font-family:"Advent Pro",sans-serif;font-weight:300;color:var(--teal);font-size:46px;line-height:1}
  .headline--one{left:250px;top:146px}
  .headline--two{left:320px;top:198px}
  .callout-lines{left:230px;top:180px}
  .keywords{left:282px;top:282px;font-family:"Pathway Gothic One",sans-serif;font-size:23px;line-height:1.02;color:var(--ink);text-transform:uppercase;list-style:none}
  .tooth-art{left:310px;top:400px;width:140px;height:180px;border-radius:40% 40% 30% 30%;background:radial-gradient(circle at 40% 35%,#ffffff,#dcdcdc 70%,#bdbdbd)}
  .services{left:24px;top:440px;width:300px}
  .services__title{font-family:"Oswald",sans-serif;font-weight:600;font-size:27px;color:var(--teal);text-transform:uppercase;letter-spacing:.5px}
  .services__list{font-family:"Pathway Gothic One",sans-serif;font-size:22px;line-height:1.2;color:var(--ink);text-transform:uppercase;margin-top:4px}
  .front-strip{left:0;top:618px;width:470px;height:22px;background:var(--teal-pale)}
  .front-band{left:0;top:640px;width:552px;height:140px;background:var(--teal)}
  .front-photos{left:18px;top:656px;display:flex;gap:12px}
  .front-photos span{display:block;width:164px;height:78px}
  .photo--exam{background:linear-gradient(120deg,#f4d2c2,#c67f66)}
  .photo--family{background:linear-gradient(120deg,#e7ecf1,#b7c7d6)}
  .photo--smile{background:linear-gradient(120deg,#cfcfcf,#e9c3b1)}
  .band-rule{left:10px;right:10px;border-top:1.5px dashed rgba(255,255,255,.85)}

  /* back */
  .back-header{left:0;top:0;width:552px;height:62px;background:var(--teal)}
  .back-tab{left:140px;top:8px;width:272px;height:50px;background:var(--white);border-radius:12px;display:flex;align-items:center;justify-content:center;gap:10px}
  .back-tab .brand{flex-direction:row;gap:10px}
  .back-tab .brand__mark{margin:0;width:28px;height:28px}
  .back-tab .brand__name{font-size:24px}
  .back-tab .brand__sub{font-size:6.5px;letter-spacing:1.5px}
  .locations{left:8px;top:66px;width:536px;display:grid;grid-template-columns:repeat(4,1fr);grid-template-rows:repeat(4,94px);list-style:none}
  .location{border-right:1.2px dashed var(--teal-mid);border-bottom:1.2px dashed var(--teal-mid);padding:8px 6px 0;text-align:center;font-size:6.6px;color:var(--ink-soft);line-height:1.35}
  .location:nth-child(4n){border-right:none}
  .location--blank{border-bottom:none}
  .location__name{color:var(--teal);font-weight:700;font-size:7.4px;margin-bottom:4px}
  .location__addr{display:flex;justify-content:center;gap:3px}
  .location__addr svg{flex:none;margin-top:1px}
  .location__phone{display:inline-flex;align-items:center;gap:3px;margin-top:5px;background:var(--teal-mid);color:#fff;font-weight:700;font-size:6.8px;border-radius:8px;padding:1.5px 9px;box-shadow:0 0 0 1.5px var(--teal-pale)}
  .back-tooth{left:28px;top:358px;width:96px;height:118px;border-radius:40% 40% 30% 30%;background:radial-gradient(circle at 40% 35%,#ffffff,#dcdcdc 70%,#bdbdbd)}
  .map{left:0;top:452px;width:552px;height:250px;background:linear-gradient(160deg,#eef0e6,#e3e8d8 45%,#b8d6ea 60%,#e9ebe0)}
  .map-wave{left:0;top:440px}
  .portrait{right:14px;top:430px;width:190px;height:270px;border-radius:60px 60px 30px 30px;border:8px solid var(--teal-soft);background:linear-gradient(160deg,#efd8c8,#8d6a58)}
  .back-band{left:0;top:700px;width:552px;height:80px;background:var(--teal)}
  .tagline{left:0;top:716px;width:552px;text-align:center;white-space:nowrap;font-family:"Antonio",sans-serif;font-weight:700;font-size:22px;line-height:30px;color:#fff;text-transform:uppercase;letter-spacing:.2px}
</style>
</head>
<body>

<section class="flyer flyer--front" aria-label="Flyer front">
  <div class="abs brand front-brand">
    <span class="brand__mark"></span>
    <span class="brand__name">The Maple Arch</span>
    <span class="brand__sub">DENTAL OFFICES</span>
  </div>

  <div class="abs call-box">
    <span class="call-box__rule"></span>
    <p class="call-box__phone">Call: 800-555-0142</p>
    <p class="call-box__web">www.maplearchsmiles.com</p>
  </div>
  <div class="abs call-box__shadow"></div>

  <div class="abs hero-photo" role="img" aria-label="Photo of a smiling woman in a dental chair"></div>

  <svg class="abs callout-lines" width="130" height="80" viewBox="0 0 130 80" aria-hidden="true">
    <polyline points="0,20 18,6 120,6" fill="none" stroke="#9a9a9a" stroke-width="1"/>
    <polyline points="0,74 30,58 100,58" fill="none" stroke="#9a9a9a" stroke-width="1"/>
  </svg>
  <p class="abs headline headline--one">Affordable</p>
  <p class="abs headline headline--two">Friendly</p>

  <ul class="abs keywords">
    <li>Experienced Dental Care</li>
    <li>Kids Friendly</li>
    <li>We Accept All Insurance</li>
    <li>0% Interest Payment Plans</li>
  </ul>

  <div class="abs tooth-art" role="img" aria-label="Glossy white 3D tooth illustration"></div>

  <div class="abs services">
    <h2 class="services__title">Dental Services:</h2>
    <p class="services__list">Family Dentistry, Teeth Whitening,<br>Braces, Implants, Veneers, Sedation.</p>
  </div>

  <div class="abs front-strip"></div>
  <div class="abs front-band"></div>
  <div class="abs front-photos">
    <span class="photo--exam" role="img" aria-label="Photo of a dental examination"></span>
    <span class="photo--family" role="img" aria-label="Photo of a dentist with a mother and child"></span>
    <span class="photo--smile" role="img" aria-label="Close-up photo of a bright smile"></span>
  </div>
  <div class="abs band-rule" style="top:756px"></div>
</section>

<section class="flyer flyer--back" aria-label="Flyer back">
  <div class="abs back-header"></div>
  <div class="abs back-tab">
    <div class="brand">
      <span class="brand__mark"></span>
      <span style="display:flex;flex-direction:column;align-items:center">
        <span class="brand__name">The Maple Arch</span>
        <span class="brand__sub">DENTAL OFFICES</span>
      </span>
    </div>
  </div>

  <ul class="abs locations">
    <li class="location"><p class="location__name">Dental Office at Lakeview Mall</p><p class="location__addr"><svg width="6" height="8" viewBox="0 0 6 8"><path d="M3 0a3 3 0 0 1 3 3c0 2-3 5-3 5S0 5 0 3a3 3 0 0 1 3-3z" fill="#33b8a4"/></svg><span>120 Lakeview St. Unit 4<br>Barrow ON</span></p><span class="location__phone">(705) 555-0101</span></li>
    <li class="location"><p class="location__name">Dental Office at Brookside Plaza</p><p class="location__addr"><svg width="6" height="8" viewBox="0 0 6 8"><path d="M3 0a3 3 0 0 1 3 3c0 2-3 5-3 5S0 5 0 3a3 3 0 0 1 3-3z" fill="#33b8a4"/></svg><span>45 Brookside Pkwy<br>Fernvale ON</span></p><span class="location__phone">(905) 555-0102</span></li>
    <li class="location"><p class="location__name">Dental Office on Elm Grove St.</p><p class="location__addr"><svg width="6" height="8" viewBox="0 0 6 8"><path d="M3 0a3 3 0 0 1 3 3c0 2-3 5-3 5S0 5 0 3a3 3 0 0 1 3-3z" fill="#33b8a4"/></svg><span>18 Elm Grove St.<br>Westbury ON</span></p><span class="location__phone">(519) 555-0103</span></li>
    <li class="location"><p class="location__name">Dental Office on Cedar St. W.</p><p class="location__addr"><svg width="6" height="8" viewBox="0 0 6 8"><path d="M3 0a3 3 0 0 1 3 3c0 2-3 5-3 5S0 5 0 3a3 3 0 0 1 3-3z" fill="#33b8a4"/></svg><span>77 Cedar St. W.<br>Ashford ON</span></p><span class="location__phone">(519) 555-0104</span></li>

    <li class="location"><p class="location__name">Dental Office on Birch St. E.</p><p class="location__addr"><svg width="6" height="8" viewBox="0 0 6 8"><path d="M3 0a3 3 0 0 1 3 3c0 2-3 5-3 5S0 5 0 3a3 3 0 0 1 3-3z" fill="#33b8a4"/></svg><span>31 Birch St. E.<br>Dunmore ON</span></p><span class="location__phone">(905) 555-0105</span></li>
    <li class="location"><p class="location__name">Dental Office on Willow Rd.</p><p class="location__addr"><svg width="6" height="8" viewBox="0 0 6 8"><path d="M3 0a3 3 0 0 1 3 3c0 2-3 5-3 5S0 5 0 3a3 3 0 0 1 3-3z" fill="#33b8a4"/></svg><span>2200 Willow Rd.<br>Oakridge ON</span></p><span class="location__phone">(416) 555-0106</span></li>
    <li class="location"><p class="location__name">Dental Office on Harbour Blvd</p><p class="location__addr"><svg width="6" height="8" viewBox="0 0 6 8"><path d="M3 0a3 3 0 0 1 3 3c0 2-3 5-3 5S0 5 0 3a3 3 0 0 1 3-3z" fill="#33b8a4"/></svg><span>300 Harbour Blvd<br>Oakridge ON</span></p><span class="location__phone">(416) 555-0107</span></li>
    <li class="location"><p class="location__name">Dental Office on Pine Rd.</p><p class="location__addr"><svg width="6" height="8" viewBox="0 0 6 8"><path d="M3 0a3 3 0 0 1 3 3c0 2-3 5-3 5S0 5 0 3a3 3 0 0 1 3-3z" fill="#33b8a4"/></svg><span>540 Pine Rd.<br>Riverton ON</span></p><span class="location__phone">(905) 555-0108</span></li>

    <li class="location"><p class="location__name">Dental Office at Midtown Mall</p><p class="location__addr"><svg width="6" height="8" viewBox="0 0 6 8"><path d="M3 0a3 3 0 0 1 3 3c0 2-3 5-3 5S0 5 0 3a3 3 0 0 1 3-3z" fill="#33b8a4"/></svg><span>377 Midtown Rd. E.<br>Riverton ON</span></p><span class="location__phone">(905) 555-0109</span></li>
    <li class="location"><p class="location__name">Dental Office on Hillcrest Rd.</p><p class="location__addr"><svg width="6" height="8" viewBox="0 0 6 8"><path d="M3 0a3 3 0 0 1 3 3c0 2-3 5-3 5S0 5 0 3a3 3 0 0 1 3-3z" fill="#33b8a4"/></svg><span>4820 Hillcrest Rd.<br>Riverton ON</span></p><span class="location__phone">(905) 555-0110</span></li>
    <li class="location"><p class="location__name">Dental Office on Meadow Rd.</p><p class="location__addr"><svg width="6" height="8" viewBox="0 0 6 8"><path d="M3 0a3 3 0 0 1 3 3c0 2-3 5-3 5S0 5 0 3a3 3 0 0 1 3-3z" fill="#33b8a4"/></svg><span>3530 Meadow Rd. E.<br>Riverton ON</span></p><span class="location__phone">(905) 555-0111</span></li>
    <li class="location"><p class="location__name">Dental Office at Northgate Plaza</p><p class="location__addr"><svg width="6" height="8" viewBox="0 0 6 8"><path d="M3 0a3 3 0 0 1 3 3c0 2-3 5-3 5S0 5 0 3a3 3 0 0 1 3-3z" fill="#33b8a4"/></svg><span>2131 Northgate Ave.<br>Eastvale ON</span></p><span class="location__phone">(416) 555-0112</span></li>

    <li class="location location--blank"></li>
    <li class="location"><p class="location__name">Dental Office at Harbour Square</p><p class="location__addr"><svg width="6" height="8" viewBox="0 0 6 8"><path d="M3 0a3 3 0 0 1 3 3c0 2-3 5-3 5S0 5 0 3a3 3 0 0 1 3-3z" fill="#33b8a4"/></svg><span>4465 Harbour Rd.<br>Eastvale ON</span></p><span class="location__phone">(416) 555-0113</span></li>
    <li class="location"><p class="location__name">Dental Office on Summit Rd.</p><p class="location__addr"><svg width="6" height="8" viewBox="0 0 6 8"><path d="M3 0a3 3 0 0 1 3 3c0 2-3 5-3 5S0 5 0 3a3 3 0 0 1 3-3z" fill="#33b8a4"/></svg><span>1590 Summit Rd.<br>Eastvale ON</span></p><span class="location__phone">(416) 555-0114</span></li>
    <li class="location"><p class="location__name">Dental Office in Clearbrook</p><p class="location__addr"><svg width="6" height="8" viewBox="0 0 6 8"><path d="M3 0a3 3 0 0 1 3 3c0 2-3 5-3 5S0 5 0 3a3 3 0 0 1 3-3z" fill="#33b8a4"/></svg><span>501 Route 8<br>Clearbrook ON</span></p><span class="location__phone">(905) 555-0115</span></li>
  </ul>

  <div class="abs map" role="img" aria-label="Regional road map with pins marking all 15 office locations"></div>
  <svg class="abs map-wave" width="552" height="40" viewBox="0 0 552 40" aria-hidden="true">
    <path d="M0 0H552V6C420 30 300 4 170 18 100 26 40 22 0 14Z" fill="#fdfdfb"/>
    <path d="M0 14C40 22 100 26 170 18 300 4 420 30 552 6" fill="none" stroke="#00a990" stroke-width="5"/>
  </svg>
  <div class="abs back-tooth" role="img" aria-label="Glossy white 3D tooth illustration"></div>
  <div class="abs portrait" role="img" aria-label="Photo of a smiling woman framed in a tooth shape"></div>

  <div class="abs back-band"></div>
  <p class="abs tagline">We're Always Close By! With 15 Locations and Counting.</p>
  <div class="abs band-rule" style="top:758px"></div>
</section>

</body>
</html>
```